Broschüre für unsere Firma
Zielgruppe
Wäscherei Kranzbeck / Textilservice
Geschäftskunden
Logos etc. In OneDrive/ Dropbox
https://ablage-beispiel.de/f/s!XkrTmWq7PzvoNeFgHsYa4Lc92_p
Wir wollen gerne eine 4 seitige Broschüre erstellen lassen, um unsere Firma vorzustellen.
Insbesondere der Service
Berufsbekleidung
Hygiene Gardienenwäsche Service
Hotelmietwäsche
Mitbewerb
http://www.wäscherei-gollwitz.de/index.php/ct-menu-item-17/ct-menu-item-25
http://www.tuch-morgen.ch/download
Im Anhang finden Sie Bilder Logo und Flyers welche wir mal selbst gemacht haben!
Datein sind im OneDrive
Aufgabenstellung

```html
<!DOCTYPE html>
<html lang="de">
<head>
<meta charset="utf-8">
<title>Wäscherei Kranzbeck – Broschüre</title>
<link rel="stylesheet" href="https://fonts.googleapis.com/css2?family=Ubuntu:wght@400;500;700&family=Source+Sans+3:ital,wght@0,400;0,600;0,700;1,600&display=swap">
<style>
  :root {
    --stage: #454545;
    --green: #7cb82f;
    --green-light: #a8d170;
    --blue: #323f96;
    --cert-green: #1d8a3f;
    --white: #ffffff;
    --photo-a: #b9b2b4;
    --photo-b: #6b7090;
  }
  html, body {
    margin: 0;
    width: 763px;
    height: 1200px;
    overflow: hidden;
    background: var(--stage);
  }
  .canvas { position: relative; width: 763px; height: 1200px; }
  .spread-label {
    position: absolute;
    left: 40px;
    margin: 0;
    font: 400 15px/1 "Ubuntu", sans-serif;
    color: var(--white);
    letter-spacing: 0.5px;
  }
  .label-outer { top: 39px; }
  .label-inner { top: 626px; }
  .spread { position: absolute; left: 27.5px; width: 706.6px; height: 499.5px; display: block; }
  .spread-outer { top: 67.1px; }
  .spread-inner { top: 654.2px; }

  .f-green { fill: var(--green); }
  .f-blue { fill: var(--blue); }
  .f-white { fill: var(--white); }
  .f-bubble { fill: var(--green-light); }
  .f-cert { fill: var(--cert-green); }

  .heading { font-family: "Ubuntu", sans-serif; font-weight: 500; letter-spacing: 1px; }
  .sans { font-family: "Source Sans 3", sans-serif; }
  .body-copy { font-family: "Source Sans 3", sans-serif; font-size: 10px; }
  .em-green { fill: var(--green); font-style: italic; font-weight: 600; }
  .em-blue { fill: var(--blue); font-style: italic; font-weight: 600; }
  .strong-green { fill: var(--green); font-weight: 700; letter-spacing: 1px; }
  .strong-blue { fill: var(--blue); font-weight: 700; letter-spacing: 1px; }
</style>
</head>
<body>
<main class="canvas">

  <h2 class="spread-label label-outer">AUSSEN</h2>

  <svg class="spread spread-outer" viewBox="0 0 1389 982" xmlns="http://www.w3.org/2000/svg">
    <defs>
      <linearGradient id="collage" x1="0" y1="0" x2="1" y2="1">
        <stop offset="0" stop-color="var(--photo-a)"/>
        <stop offset="0.55" stop-color="#d7b5bd"/>
        <stop offset="1" stop-color="var(--photo-b)"/>
      </linearGradient>
      <linearGradient id="portrait" x1="0" y1="0" x2="1" y2="1">
        <stop offset="0" stop-color="#cfcac8"/>
        <stop offset="0.5" stop-color="#e2b7c0"/>
        <stop offset="1" stop-color="#3c4a86"/>
      </linearGradient>
    </defs>

    <!-- back cover -->
    <rect class="f-white" x="0" y="0" width="1389" height="982"/>
    <polygon class="f-green" points="0,0 8,0 688,478 694,480 694,790 0,962"/>
    <polygon class="f-blue" points="22,0 72,0 694,480 690,481"/>
    <polygon class="f-blue" points="694,792 0,970 0,982 92,982"/>
    <g class="bubbles">
      <circle class="f-bubble" cx="48" cy="268" r="27"/>
      <circle class="f-bubble" cx="182" cy="291" r="23"/>
      <circle class="f-bubble" cx="124" cy="361" r="26"/>
      <circle class="f-bubble" cx="257" cy="353" r="18"/>
      <circle class="f-bubble" cx="375" cy="402" r="23"/>
      <path class="f-bubble" d="M0,353 A48,48 0 0 1 0,442 Z"/>
      <circle class="f-bubble" cx="140" cy="843" r="37"/>
      <circle class="f-bubble" cx="56" cy="901" r="25"/>
      <circle class="f-bubble" cx="245" cy="854" r="14"/>
    </g>

    <text class="heading f-blue" x="347" y="576" font-size="19" text-anchor="middle">SO ERREICHEN SIE UNS</text>
    <g class="contact sans f-white" font-size="12.5">
      <text x="263" y="636" text-anchor="middle" font-weight="700">Kontakt</text>
      <text x="263" y="660" text-anchor="middle">Lindenhofer Straße 12</text>
      <text x="263" y="677" text-anchor="middle">D-58700 Musterstadt</text>
      <text x="263" y="700" text-anchor="middle">mail@kranzbeck.info</text>
      <text x="263" y="724" text-anchor="middle">Tel. +49 (0) 2300 50410</text>
      <text x="263" y="741" text-anchor="middle">Fax. +49 (0) 2300 50419</text>
      <rect x="353" y="625" width="1.5" height="121"/>
      <text x="431" y="636" text-anchor="middle" font-weight="700">Öffnungszeiten</text>
      <text x="431" y="660" text-anchor="middle">Montag – Freitag</text>
      <text x="431" y="677" text-anchor="middle">08:00 – 17:00 Uhr</text>
    </g>

    <!-- front cover -->
    <polygon class="f-blue" points="694,0 1383,0 694,480"/>
    <polygon class="f-green" points="696,480 1389,6 1389,50"/>
    <g class="brand">
      <circle class="f-green" cx="1136" cy="398" r="20"/>
      <text class="sans f-blue" x="1164" y="406" font-size="21" font-weight="700" textLength="184" lengthAdjust="spacingAndGlyphs">Wäscherei Kranzbeck</text>
    </g>
    <rect x="694" y="480" width="695" height="310" fill="url(#collage)" role="img" aria-label="Fotocollage: Wäsche auf der Bügelmaschine, Hemden auf Bügeln, Mitarbeiterin mit verpackter Kleidung, Hemden in Folie"/>
    <polygon class="f-blue" points="694,790 1310,982 694,982"/>
    <polygon class="f-green" points="702,792 1389,935 1389,982 1350,982"/>
    <g class="certificates">
      <rect class="f-cert" x="736" y="855" width="63" height="103" rx="4"/>
      <circle class="f-cert" cx="852" cy="923" r="34"/>
    </g>
  </svg>

  <h2 class="spread-label label-inner">INNEN</h2>

  <svg class="spread spread-inner" viewBox="0 0 1389 982" xmlns="http://www.w3.org/2000/svg">
    <defs>
      <linearGradient id="portrait-inner" x1="0" y1="0" x2="1" y2="1">
        <stop offset="0" stop-color="#cfcac8"/>
        <stop offset="0.5" stop-color="#e2b7c0"/>
        <stop offset="1" stop-color="#3c4a86"/>
      </linearGradient>
    </defs>
    <rect class="f-white" x="0" y="0" width="1389" height="982"/>
    <polygon class="f-green" points="0,0 1262,0 0,184"/>
    <polygon class="f-blue" points="0,190 1292,0 1389,0 1389,12 0,195"/>
    <polygon points="0,203 694,106 694,862 0,954" fill="url(#portrait-inner)" role="img" aria-label="Foto: Mitarbeiterin prüft verpackte Kleidung in der Wäscherei"/>
    <polygon class="f-green" points="0,962 1389,774 1389,782 0,972"/>
    <polygon class="f-blue" points="0,978 1389,790 1389,982 0,982"/>

    <text class="sans f-white" font-size="15">
      <tspan x="34" y="45">Wir sind ein <tspan class="strong-blue">HYGIENEZERTIFIZIERTER</tspan></tspan>
      <tspan x="34" y="65"><tspan class="strong-blue">WÄSCHEREIBETRIEB</tspan> mit sehr viel Erfahrung</tspan>
      <tspan x="34" y="84">und Tradition: Ihre Zufriedenheit steht bei uns</tspan>
      <tspan x="34" y="104">selbstverständlich an erster Stelle und hat</tspan>
      <tspan x="34" y="123">oberste Priorität.</tspan>
    </text>

    <!-- Berufsbekleidung -->
    <text class="heading f-green" x="738" y="183" font-size="18">BERUFSBEKLEIDUNG</text>
    <g transform="translate(753,192)">
      <rect class="f-blue" width="246" height="250"/>
      <polygon class="f-green" points="0,252 246,244 246,258 0,258"/>
      <text class="body-copy f-white">
        <tspan x="11" y="19">Dies ist ein <tspan class="em-green">Typoblindtext</tspan>. An ihm kann man</tspan>
        <tspan x="11" y="34">sehen, ob alle Buchstaben da sind und wie sie</tspan>
        <tspan x="11" y="49">aussehen. Manchmal benutzt man Worte wie</tspan>
        <tspan x="11" y="65">Hamburgefonts, Rafgenduks oder Handgloves,</tspan>
        <tspan x="11" y="80">um Schriften zu testen.</tspan>
        <tspan x="11" y="110">Manchmal Sätze, die alle Buchstaben des</tspan>
        <tspan x="11" y="125">Alphabets enthalten - man nennt diese Sätze</tspan>
        <tspan x="11" y="141"><tspan class="em-green">»Pangrams«</tspan>. Sehr bekannt ist dieser: The</tspan>
        <tspan x="11" y="156">quick brown fox jumps over the lazy old dog.</tspan>
        <tspan x="11" y="171">Oft werden in Typoblindtexte auch fremd-</tspan>
        <tspan x="11" y="186">sprachige Satzteile eingebaut (AVAIL® and</tspan>
        <tspan x="11" y="201">Wefox™ are testing aussi la Kerning), um die</tspan>
        <tspan x="11" y="217"><tspan class="em-green">Wirkung in anderen Sprachen</tspan> zu testen. In La-</tspan>
        <tspan x="11" y="232">teinisch sieht zum Beispiel jede Schrift gut aus.</tspan>
      </text>
    </g>

    <!-- Hotelwäsche -->
    <text class="heading f-blue" x="1062" y="183" font-size="18">HOTELWÄSCHE</text>
    <g transform="translate(1084,192)">
      <rect class="f-green" width="246" height="250"/>
      <polygon class="f-blue" points="0,252 246,244 246,258 0,258"/>
      <text class="body-copy f-white">
        <tspan x="11" y="19">Dies ist ein <tspan class="em-blue">Typoblindtext</tspan>. An ihm kann man</tspan>
        <tspan x="11" y="34">sehen, ob alle Buchstaben da sind und wie sie</tspan>
        <tspan x="11" y="49">aussehen. Manchmal benutzt man Worte wie</tspan>
        <tspan x="11" y="65">Hamburgefonts, Rafgenduks oder Handgloves,</tspan>
        <tspan x="11" y="80">um Schriften zu testen.</tspan>
        <tspan x="11" y="110">Manchmal Sätze, die alle Buchstaben des</tspan>
        <tspan x="11" y="125">Alphabets enthalten - man nennt diese Sätze</tspan>
        <tspan x="11" y="141"><tspan class="em-blue">»Pangrams«</tspan>. Sehr bekannt ist dieser: The</tspan>
        <tspan x="11" y="156">quick brown fox jumps over the lazy old dog.</tspan>
        <tspan x="11" y="171">Oft werden in Typoblindtexte auch fremd-</tspan>
        <tspan x="11" y="186">sprachige Satzteile eingebaut (AVAIL® and</tspan>
        <tspan x="11" y="201">Wefox™ are testing aussi la Kerning), um die</tspan>
        <tspan x="11" y="217"><tspan class="em-blue">Wirkung in anderen Sprachen</tspan> zu testen. In La-</tspan>
        <tspan x="11" y="232">teinisch sieht zum Beispiel jede Schrift gut aus.</tspan>
      </text>
    </g>

    <!-- Gardinenwäsche -->
    <text class="heading f-blue" x="738" y="509" font-size="18">GARDINENWÄSCHE</text>
    <g transform="translate(753,518)">
      <rect class="f-green" width="246" height="250"/>
      <polygon class="f-blue" points="0,252 246,244 246,258 0,258"/>
      <text class="body-copy f-white">
        <tspan x="11" y="19">Dies ist ein <tspan class="em-blue">Typoblindtext</tspan>. An ihm kann man</tspan>
        <tspan x="11" y="34">sehen, ob alle Buchstaben da sind und wie sie</tspan>
        <tspan x="11" y="49">aussehen. Manchmal benutzt man Worte wie</tspan>
        <tspan x="11" y="65">Hamburgefonts, Rafgenduks oder Handgloves,</tspan>
        <tspan x="11" y="80">um Schriften zu testen.</tspan>
        <tspan x="11" y="110">Manchmal Sätze, die alle Buchstaben des</tspan>
        <tspan x="11" y="125">Alphabets enthalten - man nennt diese Sätze</tspan>
        <tspan x="11" y="141"><tspan class="em-blue">»Pangrams«</tspan>. Sehr bekannt ist dieser: The</tspan>
        <tspan x="11" y="156">quick brown fox jumps over the lazy old dog.</tspan>
        <tspan x="11" y="171">Oft werden in Typoblindtexte auch fremd-</tspan>
        <tspan x="11" y="186">sprachige Satzteile eingebaut (AVAIL® and</tspan>
        <tspan x="11" y="201">Wefox™ are testing aussi la Kerning), um die</tspan>
        <tspan x="11" y="217"><tspan class="em-blue">Wirkung in anderen Sprachen</tspan> zu testen. In La-</tspan>
        <tspan x="11" y="232">teinisch sieht zum Beispiel jede Schrift gut aus.</tspan>
      </text>
    </g>

    <!-- Weitere Services -->
    <text class="heading f-green" x="1062" y="509" font-size="18">WEITERE SERVICES</text>
    <g transform="translate(1084,518)">
      <rect class="f-blue" width="246" height="250"/>
      <polygon class="f-green" points="0,252 246,244 246,258 0,258"/>
      <g class="ticks" fill="none" stroke="var(--green)" stroke-width="1.6">
        <path d="M12,16 l3,3 l5,-7"/>
        <path d="M12,31 l3,3 l5,-7"/>
        <path d="M12,46 l3,3 l5,-7"/>
        <path d="M12,62 l3,3 l5,-7"/>
        <path d="M12,77 l3,3 l5,-7"/>
        <path d="M12,92 l3,3 l5,-7"/>
        <path d="M12,107 l3,3 l5,-7"/>
        <path d="M12,122 l3,3 l5,-7"/>
        <path d="M12,138 l3,3 l5,-7"/>
        <path d="M12,153 l3,3 l5,-7"/>
        <path d="M12,168 l3,3 l5,-7"/>
        <path d="M12,183 l3,3 l5,-7"/>
        <path d="M12,198 l3,3 l5,-7"/>
        <path d="M12,214 l3,3 l5,-7"/>
        <path d="M12,229 l3,3 l5,-7"/>
      </g>
      <text class="body-copy f-white">
        <tspan x="32" y="20">Altenheimwäsche</tspan>
        <tspan x="32" y="35">Flammschutzausrüstung</tspan>
        <tspan x="32" y="50">Gastronomiewäsche</tspan>
        <tspan x="32" y="66">Haushaltswäsche</tspan>
        <tspan x="32" y="81">Imprägnierservice</tspan>
        <tspan x="32" y="96">Kittelservice</tspan>
        <tspan x="32" y="111">Lamellenreinigung</tspan>
        <tspan x="32" y="126">Mangelwäsche</tspan>
        <tspan x="32" y="142">Oberbetten / Kissen / Wasserbetten</tspan>
        <tspan x="32" y="157">Oberhemden</tspan>
        <tspan x="32" y="172">Pferdedecken</tspan>
        <tspan x="32" y="187">Teppichreinigung</tspan>
        <tspan x="32" y="202">Textilreinigung</tspan>
        <tspan x="32" y="218">Wascheraumhygiene</tspan>
        <tspan x="32" y="233">Hol- und Bringservice</tspan>
      </text>
    </g>

    <text class="sans f-white" font-size="15" text-anchor="end">
      <tspan x="1363" y="890">Ihre Wäsche wird nicht nur <tspan class="strong-green">STRAHLEND SAUBER,</tspan></tspan>
      <tspan x="1363" y="910">sondern auch ökologisch und ökonomisch einwandfrei behandelt.</tspan>
      <tspan x="1363" y="929"><tspan class="strong-green">QUALIFIZIERTE MITARBEITER</tspan> und <tspan class="strong-green">MODERNSTE TECHNIK</tspan></tspan>
      <tspan x="1363" y="949">gewährleisten ein gleichbleibend hohes Niveau unserer Arbeit.</tspan>
    </text>
  </svg>

</main>
</body>
</html>
```